Small legal and financial translation company needs Squarespace website, brochure and logo

Hello,
We are LMV Services (www.lmvservices-example.com), a boutique legal and financial translation company. We offer our services mainly to Spanish customers. Our primary line of business is the translation of financial statements, but we translate a wide variety legal and financial texts.
The project we are offering comprises three parts: a redo of the current website, an informational brochure for potential customer and a logo design. These three parts should provide a consistent image. We would develop content soon.
We are looking for a website that would look like a typical law firm website, nothing too fancy. Right now, it is in English, Spanish and French, although the new site need only be in English and Spanish. There must be good toggling between the English and Spanish versions. There would be no need for tie-ins to social media and it would not contain a blog. Basically, a static site. We aren't interesting in driving traffic to the site or SEO, as we will contact nearly all potential customers beforehand. The website must be built in Squarespace to enable a smooth transition. The content would be similar to the current page, we'll be working on the exact content, but a rough draft is attached.
The brochure will be some three pages and would introduce the company to potential customers, using similar images as the website and the logo to be designed.
The only specifications for the logo is, as the website and brochure, it convey a sense of security and trust.
Feel free to ask with any questions as this is the first time we have used this platform.
Thank you!
Updates

I've added a more or less final version for the text in the brochure and updated the brief. Added Wednesday, June 10, 2015

Target Market(s)

Spanish law firms, auditors, accountants, banks, investment firms

Industry/Entity Type

Finance

Logo Text

LMV Services

Number of Pages Required

5+ page

Font styles to use
Serif

Requirements
Must have
• The website must be built in Squarespace and have a good option to toggle between English and Spanish versions.
• Brochure must be in both English and Spanish, I'm attaching a rough draft of the information that it will probably have. This should give an idea about what to include and the spacing. I will update it to include the final information.
Nice to have
• Would be nice to have some quality finance- and legal-related images
Should not have
• Vibrant colours

```html
<!DOCTYPE html>
<html lang="en">
<head>
<meta charset="utf-8">
<title>LMV Services – Brochure Page 5</title>
<link rel="stylesheet" href="https://fonts.googleapis.com/css2?family=Cinzel:wght@400&family=Crimson+Text:ital,wght@0,400;0,700&family=Open+Sans:wght@400&display=swap">
<style>
  :root {
    --backdrop: #cccccc;
    --paper: #ffffff;
    --navy: #2a4282;
    --ink: #1d1d1d;
    --black: #000000;
    --label: #333333;
  }
  html, body {
    margin: 0;
    padding: 0;
    width: 1200px;
    height: 1200px;
    overflow: hidden;
    background: var(--backdrop);
  }
  .canvas {
    position: relative;
    width: 1200px;
    height: 1200px;
  }
  .page-label {
    position: absolute;
    top: 34px;
    left: 0;
    width: 1240px;
    text-align: center;
    font-family: "Open Sans", sans-serif;
    font-size: 34px;
    color: var(--label);
    margin: 0;
  }
  .sheet {
    position: absolute;
    left: 268px;
    top: 110px;
    width: 699px;
    height: 991px;
    background: var(--paper);
    box-shadow: 0 2px 14px rgba(0,0,0,0.35);
    overflow: hidden;
  }
  .sheet-title {
    position: absolute;
    left: 41px;
    top: 48px;
    margin: 0;
    font-family: "Cinzel", serif;
    font-weight: 400;
    font-size: 31px;
    line-height: 37px;
    letter-spacing: 1.2px;
    color: var(--navy);
  }
  .benefits {
    position: absolute;
    left: 47px;
    top: 196px;
    width: 608px;
    font-family: "Crimson Text", serif;
    font-size: 13.4px;
    line-height: 19.5px;
    color: var(--ink);
    letter-spacing: -0.35px;
  }
  .benefit { margin: 0 0 37px; }
  .benefit-heading {
    margin: 0;
    font-weight: 700;
    font-size: 14px;
    color: var(--black);
  }
  .benefit-text {
    margin: 0;
    text-align: justify;
  }
  .footer-art {
    position: absolute;
    left: 0;
    top: 0;
    width: 699px;
    height: 991px;
  }
  .site-url {
    position: absolute;
    left: 24px;
    top: 952px;
    margin: 0;
    font-family: "Crimson Text", serif;
    font-size: 19px;
    color: var(--paper);
  }
</style>
</head>
<body>
<main class="canvas">
  <p class="page-label">Page 5</p>

  <article class="sheet">
    <h1 class="sheet-title">Benefits of working with a<br>specialist translation company<br>rather than a translation agency</h1>

    <section class="benefits">
      <div class="benefit">
        <h2 class="benefit-heading">Quality.:</h2>
        <p class="benefit-text">Translation agencies cannot guarantee that the same translator will always work on your projects, which means customers might receive inconsistent and poorer quality translations depending on the availability of the agency’s translators. At LMV Services, you personally know who is working on your project and can attest the quality of their work.</p>
      </div>
      <div class="benefit">
        <h2 class="benefit-heading">Pricing.:</h2>
        <p class="benefit-text">LMV Services provides the same high-quality services as the leading in-house translation departments in Spain, at a fraction of the price. Our quality control process affords highly polished finished products at reasonable prices. Our low overheads mean that we do not pass on a exorbitant cost structure to our customers. Agencies and the translation departments in Spain’s leading law and auditing firms have much higher fixed costs that entail higher prices for the customer.</p>
      </div>
      <div class="benefit">
        <h2 class="benefit-heading">Honesty:</h2>
        <p class="benefit-text">From time to time, certain projects simply are too big, too urgent or too complex to undertake in the conditions required by our customers. Agencies are capable of handling multi-language projects with ultra-tight deadlines. This inevitably decreases the quality and consistency of our work. We work closely with our customers to set deadlines that ensure quality while respecting the urgency of their affairs.</p>
      </div>
    </section>

    <svg class="footer-art" viewBox="0 0 699 991" aria-hidden="false">
      <defs>
        <linearGradient id="photo-tone" x1="0" y1="0" x2="1" y2="1">
          <stop offset="0" stop-color="#3a3a3a"/>
          <stop offset="0.45" stop-color="#9a9a9a"/>
          <stop offset="1" stop-color="#5a5a5a"/>
        </linearGradient>
      </defs>
      <rect class="photo-area" role="img" aria-label="Black and white photo of a judge's gavel beside hands signing a legal document" x="0" y="620" width="699" height="371" fill="url(#photo-tone)"/>
      <polygon class="band-black" points="0,628 82,625 490,690 0,712" fill="var(--black)"/>
      <polygon class="band-navy" points="102,625 699,598 699,712" fill="var(--navy)"/>
      <line x1="90" y1="625" x2="699" y2="712" stroke="var(--paper)" stroke-width="3"/>
      <polygon class="accent-navy" points="530,935 660,880 672,922" fill="var(--navy)"/>
      <polygon class="band-black" points="350,957 699,920 699,986" fill="var(--black)"/>
      <polygon class="band-navy" points="0,924 699,988 699,991 0,991" fill="var(--navy)"/>
      <line x1="0" y1="922" x2="699" y2="986" stroke="var(--paper)" stroke-width="3"/>
      <line x1="350" y1="957" x2="699" y2="920" stroke="var(--paper)" stroke-width="2"/>
    </svg>

    <p class="site-url">www.lmvservices-example.com</p>
  </article>
</main>
</body>
</html>
```